kestrova business cards

Hey design gurus!
I'm after a clean, modern, stylish business card for my about to be launched company.
I've uploaded the logos for my company "Kestrova Electrical Solutions"
and also the tarrow alliance logo to whom i am associated.

```html
<!DOCTYPE html>
<html lang="en">
<head>
<meta charset="utf-8">
<title>Kestrova Electrical Solutions – Business Cards</title>
<link href="https://fonts.googleapis.com/css2?family=Montserrat:wght@400;500;700;800&display=swap" rel="stylesheet">
<style>
  :root{
    --stage:#2b2b2b;
    --card:#03151e;
    --blue:#1788d6;
    --white:#f2f5f7;
    --muted:#c9d3da;
  }
  *{box-sizing:border-box;margin:0;padding:0}
  html,body{width:1200px;height:875px;overflow:hidden}
  body{background:var(--stage);font-family:"Montserrat",sans-serif;position:relative}
  .card{
    position:absolute;left:280px;width:640px;height:366px;
    background:var(--card);border-radius:26px;
    box-shadow:0 18px 40px rgba(0,0,0,.55);
  }
  .card--front{top:40px}
  .card--back{top:469px}

  .brand{display:flex;align-items:center;gap:18px;position:absolute}
  .brand__dot{width:62px;height:62px;border-radius:50%;background:var(--blue);flex:none}
  .brand__name{color:var(--blue);font-weight:800;text-transform:uppercase;line-height:1.05;letter-spacing:.5px}
  .brand__name span{display:block}
  .brand__name .big{font-size:44px;letter-spacing:2px}
  .brand__name .small{font-size:15px;letter-spacing:4.3px}

  .card--front .brand{left:118px;top:140px}
  .partner-badge{
    position:absolute;right:44px;bottom:44px;width:110px;height:50px;
    border:1.5px solid var(--white);border-radius:6px;
    display:flex;align-items:center;padding-left:10px;
  }
  .partner-badge__tile{width:28px;height:28px;background:var(--white);border-radius:3px}

  .card--back .brand{left:60px;top:62px}
  .card--back .brand__dot{width:56px;height:56px}
  .card--back .brand__name .big{font-size:38px}
  .card--back .brand__name .small{font-size:13px;letter-spacing:3.7px}

  .person{position:absolute;left:60px;top:198px;width:320px}
  .person__name{color:var(--blue);font-weight:700;font-size:26px;letter-spacing:1px;text-transform:uppercase;white-space:nowrap}
  .person__role{color:var(--white);font-weight:400;font-size:15px;letter-spacing:1.5px;text-transform:uppercase;margin-top:4px}
  .address{position:absolute;left:60px;top:296px;color:var(--white);font-size:15px}

  .divider{position:absolute;left:398px;top:182px;width:1.5px;height:82px;background:var(--blue)}
  .contacts{position:absolute;left:416px;top:184px;list-style:none;color:var(--white);font-size:14px}
  .contacts li{display:flex;align-items:center;gap:10px;height:26px;white-space:nowrap}
  .contacts svg{width:14px;height:14px;flex:none}
</style>
</head>
<body>

<section class="card card--front" aria-label="Card front">
  <div class="brand">
    <div class="brand__dot"></div>
    <div class="brand__name"><span class="big">Kestrova</span><span class="small">Electrical Solutions</span></div>
  </div>
  <div class="partner-badge" role="img" aria-label="Tarrow Alliance partner badge">
    <div class="partner-badge__tile"></div>
  </div>
</section>

<section class="card card--back" aria-label="Card back">
  <div class="brand">
    <div class="brand__dot"></div>
    <div class="brand__name"><span class="big">Kestrova</span><span class="small">Electrical Solutions</span></div>
  </div>

  <div class="person">
    <p class="person__name">Callum Brennick</p>
    <p class="person__role">Managing Director</p>
  </div>

  <div class="divider"></div>
  <ul class="contacts">
    <li>
      <svg viewBox="0 0 24 24" fill="#f2f5f7"><path d="M6.6 10.8a15 15 0 0 0 6.6 6.6l2.2-2.2a1 1 0 0 1 1-.25 11.4 11.4 0 0 0 3.6.57 1 1 0 0 1 1 1V20a1 1 0 0 1-1 1A17 17 0 0 1 3 4a1 1 0 0 1 1-1h3.5a1 1 0 0 1 1 1c0 1.25.2 2.45.57 3.57a1 1 0 0 1-.25 1z"/></svg>
      044-718 302 645
    </li>
    <li>
      <svg viewBox="0 0 24 24"><path d="M2 5h20v14H2z" fill="none" stroke="#f2f5f7" stroke-width="2"/><path d="M2 5l10 8 10-8" fill="none" stroke="#f2f5f7" stroke-width="2"/></svg>
      info@kestrova-es.com
    </li>
    <li>
      <svg viewBox="0 0 24 24" fill="none" stroke="#f2f5f7" stroke-width="2"><circle cx="12" cy="12" r="10"/><path d="M2 12h20M12 2c3 3 3 17 0 20M12 2c-3 3-3 17 0 20"/></svg>
      www.kestrova-es.com
    </li>
  </ul>

  <p class="address">18 Harlow Yard, Elmstead 45210, Northland</p>
</section>

</body>
</html>
```